Business Cards for an 'affordable luxury' inner city home builder in Calgary.

We need a business card design that emulates the progressive, innovative, culture of our company and the modern style of our homes. Use our website www.velmarbuilds-ex.com as a reference for the product we build.

Our company builds homes in the inner city space of Calgary, Alberta. We build affordable luxury.

Target Market(s)

Young professional Families

Contact Information for Business Card

Try to maintain consistency with the logo font and the card font.

Requirements
Must have
• The details must include: Name, education, title, phone number, website and email (Address is not as important)
• The design must be uniques (like our logo), elegant, sophisticated and modern.

```html
<!DOCTYPE html>
<html lang="en">
<head>
<meta charset="utf-8">
<title>Velmar Custom Homes – Business Card</title>
<link rel="stylesheet" href="https://fonts.googleapis.com/css2?family=Roboto+Condensed:wght@400;700&display=swap">
<style>
  :root {
    --page-bg: #e4e4e4;
    --card-white: #ffffff;
    --card-dark: #232323;
    --ink-dark: #222222;
    --accent-grey: #8a8a8a;
    --text-light: #ffffff;
    --pattern-a: #282828;
    --pattern-b: #1d1d1d;
  }
  * { box-sizing: border-box; margin: 0; padding: 0; }
  html, body {
    width: 1125px; height: 1200px; overflow: hidden;
    background: var(--page-bg);
    font-family: "Roboto Condensed", "Arial Narrow", sans-serif;
  }
  .card {
    position: absolute; left: 150px; width: 826px; height: 471px; overflow: hidden;
  }
  .card--front { top: 98px; background: var(--card-white); }
  .card--back { top: 631px; background: var(--card-dark); }

  .front__bar {
    position: absolute; left: 0; top: 101px; width: 21px; height: 293px;
    background: var(--accent-grey);
  }
  .front__brand {
    position: absolute; left: 36px; top: 205px;
    display: flex; align-items: center; gap: 26px;
  }
  .brand__square {
    width: 70px; height: 70px; background: var(--ink-dark);
  }
  .brand__name {
    color: var(--ink-dark); font-weight: 400; font-size: 31px;
    line-height: 31px; letter-spacing: 1.5px; text-transform: uppercase;
  }
  .front__panel {
    position: absolute; left: 421px; top: 101px; width: 405px; height: 293px;
    background: var(--card-dark); color: var(--text-light);
    text-align: right; padding: 24px 41px 0 0;
  }
  .contact__name { font-weight: 700; font-size: 31px; line-height: 34px; }
  .contact__title { font-size: 20px; line-height: 24px; margin-bottom: 8px; }
  .contact__role { font-size: 19.5px; line-height: 25px; }
  .contact__details { margin-top: 24px; font-size: 21px; line-height: 26px; }
  .contact__line { display: flex; justify-content: flex-end; align-items: center; gap: 8px; }
  .contact__icon { width: 15px; height: 15px; fill: var(--text-light); }

  .back__pattern {
    position: absolute; inset: 0;
    background: linear-gradient(160deg, var(--pattern-a), var(--pattern-b));
  }
  .back__brand {
    position: absolute; right: 38px; bottom: 96px;
    color: var(--text-light); font-size: 26px; line-height: 28px;
    letter-spacing: 1.5px; text-transform: uppercase; text-align: right;
  }
  .back__web {
    position: absolute; right: 38px; bottom: 46px;
    color: var(--text-light); font-size: 19px;
  }
</style>
</head>
<body>
  <section class="card card--front">
    <div class="front__bar"></div>
    <div class="front__brand">
      <div class="brand__square"></div>
      <div class="brand__name">Velmar<br>Custom<br>Homes Ltd</div>
    </div>
    <div class="front__panel">
      <div class="contact__name">Daveen</div>
      <div class="contact__title">Co-Founder</div>
      <div class="contact__role">Business Development / Strategy</div>
      <div class="contact__role">Professional Engineer (P.ENG)</div>
      <div class="contact__role">Masters of Business Administration (MBA)</div>
      <div class="contact__details">
        <div class="contact__line">742 18 Ave NE, Calgary, AB</div>
        <div class="contact__line">403-555-0148
          <svg class="contact__icon" viewBox="0 0 24 24" aria-hidden="true"><path d="M6.6 10.8a15.2 15.2 0 0 0 6.6 6.6l2.2-2.2a1 1 0 0 1 1-.25 11.4 11.4 0 0 0 3.6.57 1 1 0 0 1 1 1V20a1 1 0 0 1-1 1A17 17 0 0 1 3 4a1 1 0 0 1 1-1h3.5a1 1 0 0 1 1 1c0 1.25.2 2.45.57 3.6a1 1 0 0 1-.25 1z"/></svg>
        </div>
        <div class="contact__line">projects@velmarbuilds-ex.com
          <svg class="contact__icon" viewBox="0 0 24 24" aria-hidden="true"><path d="M2 5h20v14H2z M3 6l9 7 9-7" fill="none" stroke="#fff" stroke-width="0"/><path d="M2 6h20v13H2zM3.5 7.5 12 13.5l8.5-6" /></svg>
        </div>
      </div>
    </div>
  </section>

  <section class="card card--back">
    <div class="back__pattern" role="img" aria-label="Embossed repeating pattern of the company's building mark across the dark card"></div>
    <div class="back__brand">Velmar<br>Custom Homes</div>
    <div class="back__web">www.velmarbuilds-ex.com</div>
  </section>
</body>
</html>
```